Design logo, business cards and letterhead for my eye surgery (doctor's) practice

I am a young eye surgeon (Ophthalmic Surgeon) and I need business cards and letterhead designed ( I have a business card brief and a stationary brief submitted). A small logo would also be useful, or some shape that is seen on both the cards and the letterhead. I am based in Perth, Western Australia. I do some laser refractive work ie LASIK, but also other aspects of ophthalmology as well. The design should be conservative, professional and classic, but also, (as someone who sees young patients for laser surgery) a little interesting to people who refer to me and to patients who will be given my card. The details on the letterhead should be:
Dr Ned Palliser
MBBS (Hons), MMed, FRANZCO
Ophthalmic Surgeon

27 Waverton Ave, Subiaco
Western Australia 6008
Phone: (08) 9217 4602
Facsimile: (08) 9217 4619
Email: reception@nedpalliser.com.au
Provider No: 618095KW

The information on the cards should be the same, but with out the provider number.
On the back of the card should say-

Next Appointment________
The rooms can be accessed easily via public transport, or please feel free to park behind the premises in the designated parking bays.

Target Market(s)

General practitioners and optometrists who refer to me and patients

Industry/Entity Type

Business

Contact Information for Business Card

See above

Requirements
Nice to have
• I've attached a little photo which I thought may make a cute logo of sorts on the cards and letterhead.

```html
<!DOCTYPE html>
<html lang="en">
<head>
<meta charset="utf-8">
<title>Dr. Ned Palliser – Letterhead</title>
<link rel="stylesheet" href="https://fonts.googleapis.com/css2?family=Tinos:wght@400;700&family=Fredoka:wght@700&display=swap">
<style>
  :root {
    --paper: #ffffff;
    --ink: #111111;
    --name-red: #ff3b2f;
    --cred-blue: #1f2fd6;
    --badge-green: #4fe31f;
    --mark-blue: #1c3fd8;
    --mark-pink: #e21fb8;
  }
  html, body {
    margin: 0;
    padding: 0;
    overflow: hidden;
  }
  body {
    width: 900px;
    height: 1200px;
    background: var(--paper);
    position: relative;
    font-family: "Tinos", "Times New Roman", serif;
    color: var(--ink);
  }
  .practice-mark {
    position: absolute;
    left: 70px;
    top: 100px;
    width: 200px;
    height: 90px;
    display: flex;
    align-items: center;
    gap: 12px;
  }
  .practice-mark__dot {
    width: 58px;
    height: 58px;
    border-radius: 50%;
    background: var(--mark-blue);
    flex: none;
  }
  .practice-mark__name {
    font-family: "Tinos", "Times New Roman", serif;
    font-weight: 700;
    font-size: 22px;
    line-height: 1.1;
    color: var(--mark-pink);
  }
  .doctor-name {
    position: absolute;
    left: 343px;
    top: 95px;
    width: 477px;
    height: 65px;
    margin: 0;
    background: var(--name-red);
    color: #ffffff;
    font-weight: 700;
    font-size: 56px;
    line-height: 68px;
    text-align: center;
    letter-spacing: 1px;
    white-space: nowrap;
    overflow: hidden;
  }
  .credentials {
    position: absolute;
    left: 440px;
    top: 161px;
    width: 382px;
    margin: 0;
    text-align: right;
    color: var(--cred-blue);
    font-size: 24px;
    line-height: 28px;
    white-space: nowrap;
  }
  .specialty {
    position: absolute;
    left: 540px;
    top: 191px;
    width: 280px;
    height: 35px;
    margin: 0;
    background: var(--badge-green);
    color: #ffffff;
    font-family: "Fredoka", "Arial Rounded MT Bold", sans-serif;
    font-weight: 700;
    font-size: 26px;
    line-height: 36px;
    text-align: center;
    white-space: nowrap;
  }
  .rule {
    position: absolute;
    left: 50px;
    width: 819px;
    height: 0;
    border-top: 2px solid var(--ink);
  }
  .rule--top { top: 234px; }
  .rule--bottom { top: 287px; }
  .contact {
    position: absolute;
    left: 50px;
    top: 241px;
    width: 819px;
    margin: 0;
    font-style: normal;
    font-size: 17px;
    line-height: 20px;
    text-align: center;
    white-space: nowrap;
  }
  .contact__line { display: block; }
  .contact__gap { display: inline-block; width: 24px; }
  .contact__gap--narrow { width: 14px; }
</style>
</head>
<body>
  <header class="letterhead">
    <div class="practice-mark">
      <span class="practice-mark__dot"></span>
      <span class="practice-mark__name">Ned Palliser</span>
    </div>
    <h1 class="doctor-name">Dr. Ned Palliser</h1>
    <p class="credentials">MBBS (Hons), MMed, FRANZCO</p>
    <p class="specialty">Ophthalmic Surgeon</p>
    <div class="rule rule--top"></div>
    <address class="contact">
      <span class="contact__line">27 Waverton Ave, Kellsbury, Westland 6091<span class="contact__gap"></span>Phone: (08) 9217 4602 Facsimile: (08) 9217 4619</span>
      <span class="contact__line">Email: reception@nedpalliser.com.au<span class="contact__gap contact__gap--narrow"></span>Provider No: 618095KW</span>
    </address>
    <div class="rule rule--bottom"></div>
  </header>
</body>
</html>
```